Business Card, Letterhead, Envelopes, Thank you cards, Post Cards
Business cards and stationary for life coach
Professional
Silver Heron Guidance Studio
Marla Penrick, MA
4810 North Calloway Avenue
Suite C 240
Missoula, Montana 59417
silverheronguidance@mailbox-example.net
silverheronguidance-example.com
I would like to see 'Let Your Dreams Take Flight' on the front of the card. This is the tagline. Please use a compatible font with the logo.
'Dragonfly spends most of her life underwater until the day she discovers her wings and soars upon the wind.' I'd like to see this in script, similar to the logo font.
Please let me know if you need different files.

```html
<!DOCTYPE html>
<html lang="en">
<head>
<meta charset="utf-8">
<title>Silver Heron Guidance Studio – Business Card</title>
<link href="https://fonts.googleapis.com/css2?family=Noto+Serif:ital,wght@0,400;0,700;1,700&display=swap" rel="stylesheet">
<style>
  :root {
    --stage: #e9ebee;
    --card-white: #ffffff;
    --brand-blue: #1f73c2;
    --deep-blue: #1659a6;
    --band-blue: #2a78c9;
    --light-wave: #8cc8f0;
    --text-light: #ffffff;
    --shadow: rgba(20, 40, 70, 0.25);
  }
  * { box-sizing: border-box; margin: 0; padding: 0; }
  html, body {
    width: 1200px;
    height: 780px;
    overflow: hidden;
    background: var(--stage);
    font-family: "Noto Serif", Georgia, serif;
  }
  .business-card {
    position: absolute;
    left: 100px;
    top: 100px;
    width: 1000px;
    height: 580px;
    border-radius: 40px;
    overflow: hidden;
    background: var(--card-white);
    box-shadow: 0 18px 40px var(--shadow);
  }
  .card-waves {
    position: absolute;
    inset: 0;
    width: 100%;
    height: 100%;
  }
  .brand-lockup {
    position: absolute;
    left: 160px;
    top: 150px;
    display: flex;
    align-items: center;
    gap: 18px;
  }
  .brand-dot {
    width: 26px;
    height: 26px;
    border-radius: 50%;
    background: var(--brand-blue);
  }
  .brand-name {
    font-size: 46px;
    font-weight: 400;
    color: var(--brand-blue);
    letter-spacing: 0.5px;
  }
  .holder-block {
    position: absolute;
    right: 530px;
    top: 385px;
    text-align: right;
    color: var(--text-light);
  }
  .holder-name {
    font-size: 30px;
    font-weight: 700;
    font-style: italic;
    margin-bottom: 26px;
  }
  .holder-address {
    font-size: 21px;
    line-height: 1.45;
  }
  .divider {
    position: absolute;
    left: 500px;
    top: 352px;
    width: 2px;
    height: 180px;
    background: var(--text-light);
    opacity: 0.85;
  }
  .contact-list {
    position: absolute;
    left: 522px;
    top: 355px;
    list-style: none;
    color: var(--text-light);
    font-size: 21px;
  }
  .contact-item {
    display: flex;
    align-items: center;
    gap: 12px;
    height: 38px;
  }
  .contact-icon {
    width: 22px;
    height: 22px;
    flex: none;
  }
</style>
</head>
<body>
  <div class="business-card">
    <svg class="card-waves" viewBox="0 0 1000 580" preserveAspectRatio="none" aria-hidden="true">
      <defs>
        <linearGradient id="bandFill" x1="0" y1="0" x2="0" y2="1">
          <stop offset="0" stop-color="#3a88d4"/>
          <stop offset="1" stop-color="#1659a6"/>
        </linearGradient>
      </defs>
      <path d="M0 300 C 220 250, 420 330, 640 300 S 900 250, 1000 262 L1000 580 L0 580 Z" fill="#8cc8f0"/>
      <path d="M0 322 C 230 280, 430 350, 650 318 S 900 275, 1000 285 L1000 580 L0 580 Z" fill="url(#bandFill)"/>
    </svg>

    <div class="brand-lockup">
      <span class="brand-dot"></span>
      <span class="brand-name">Silver Heron Guidance Studio</span>
    </div>

    <div class="holder-block">
      <p class="holder-name">Marla Penrick, MA</p>
      <p class="holder-address">4810 North Calloway Avenue, Suite C 240<br>Missoula, Montana 59417</p>
    </div>

    <div class="divider"></div>

    <ul class="contact-list">
      <li class="contact-item">
        <svg class="contact-icon" viewBox="0 0 24 24" aria-label="Phone"><path fill="#fff" d="M6.6 10.8a15 15 0 0 0 6.6 6.6l2.2-2.2a1 1 0 0 1 1-.25 11 11 0 0 0 3.6.6 1 1 0 0 1 1 1V20a1 1 0 0 1-1 1A17 17 0 0 1 3 4a1 1 0 0 1 1-1h3.5a1 1 0 0 1 1 1 11 11 0 0 0 .6 3.6 1 1 0 0 1-.25 1z"/></svg>
        <span>406-555-0142</span>
      </li>
      <li class="contact-item">
        <svg class="contact-icon" viewBox="0 0 24 24" aria-label="Email"><circle cx="12" cy="12" r="11" fill="#fff"/><rect x="6" y="8" width="12" height="8" rx="1" fill="none" stroke="#1659a6" stroke-width="1.6"/><path d="M6.5 8.5 12 13l5.5-4.5" fill="none" stroke="#1659a6" stroke-width="1.6"/></svg>
        <span>silverheronguidance@mailbox-example.net</span>
      </li>
      <li class="contact-item">
        <svg class="contact-icon" viewBox="0 0 24 24" aria-label="Website"><circle cx="12" cy="12" r="11" fill="#fff"/><g fill="none" stroke="#1659a6" stroke-width="1.4"><circle cx="12" cy="12" r="6.5"/><ellipse cx="12" cy="12" rx="3" ry="6.5"/><path d="M5.5 12h13"/></g></svg>
        <span>silverheronguidance-example.com</span>
      </li>
    </ul>
  </div>
</body>
</html>
```